Rebrand/migrate of website to Wordpress

Rebrand/transfer of php website to new wordpress website using the Noxel theme. Dial4LessLines.com is being rebranded to Quorvix and therefore we are looking to simplify the current layout to match competitors sites and be mobile device friendly.
The new site will need to show services in a clear uncluttered way with more emphasis on the service rather than large amounts of text. See attachment B1 for example.
Competitors sites are kx.com , ringmoor.co.uk, zelwire.com
Updates

As I have had a few request from designers to extend the deadline. I have requested Pixel Harbor to extend to Tuesday 3rd April 2018

Target Market(s)

UK Home phone and small business customers

Industry/Entity Type

Telecom

Coding

Coded - Design and coding required

Number of Pages Required

5+ page

Colors

Designer to choose colors to be used in the design.

Requirements
Must have
• 1. Use Noxel wordpress theme that will be supplied.
• 2. Combine the best layouts where possible as used by competitors but in a unique way.
• 3. Horizontal bar should be in white so that it can layer over banner as per file A1.
• 4. Simplify current layout to match competitors see attached file B1.
• 5. Integrate Tallbranch - Tallbranch Leads Web / web form to capture interested customers - name, Company name, Telephone number, email address.
Should not have
• Colour scheme that is the same as our competitors RingMoor, KX, Halden, Vexa Net

```html
<!DOCTYPE html>
<html lang="en">
<head>
<meta charset="utf-8">
<title>Quorvix — Switch To Cheaper Calls</title>
<link href="https://fonts.googleapis.com/css2?family=Poppins:wght@300;400;500;600&family=Roboto+Condensed:wght@300;400;700&display=swap" rel="stylesheet">
<style>
:root{
  --orange:#f7931e;
  --cyan:#1ab0e6;
  --magenta:#d0197f;
  --green:#7cc242;
  --ink:#2b2b2b;
  --muted:#777;
  --soft:#f6f6f6;
  --topbar:#5b5b5b;
  --footer:#222;
  --footer-dark:#1a1a1a;
  --white:#fff;
}
*{box-sizing:border-box;margin:0;padding:0}
html,body{width:1200px;height:3321px;overflow:hidden}
body{font-family:"Poppins",sans-serif;color:var(--ink);background:var(--white);position:relative}
section,header,footer{position:absolute;left:0;width:1200px}
.abs{position:absolute}

/* top bar */
.topbar{top:0;height:33px;background:var(--topbar);color:var(--white);font-size:12px;font-weight:600;letter-spacing:.3px}
.topbar .order{left:113px;top:9px}
.topbar .order b{font-size:15px;margin-left:4px}
.topbar .account{right:113px;top:0;height:33px;width:110px;background:#4a4a4a;display:flex;align-items:center;justify-content:center;gap:8px;font-size:10px}

/* nav */
.nav{top:33px;height:78px;background:var(--white)}
.brand{left:113px;top:20px;font-family:"Poppins",sans-serif;font-size:34px;font-weight:500;color:var(--orange);letter-spacing:-.5px}
.menu{right:113px;top:30px;display:flex;gap:53px;font-size:13px;color:var(--ink);list-style:none}
.menu .active{color:var(--orange)}

/* hero */
.hero{top:111px;height:602px;overflow:hidden}
.hero-photo{position:absolute;inset:0;background:linear-gradient(100deg,#3b2e25 0%,#6b5443 35%,#a88569 60%,#c8a88c 80%,#8c6d55 100%)}
.hero h1{position:absolute;left:113px;top:108px;font-family:"Roboto Condensed",sans-serif;font-weight:700;font-size:60px;line-height:72px;color:var(--cyan)}
.hero p{position:absolute;left:113px;top:268px;width:520px;color:var(--white);font-size:17px;line-height:35px;font-weight:500}
.btn{display:inline-flex;align-items:center;justify-content:center;border-radius:30px;font-size:12px;font-weight:600;letter-spacing:.5px;text-transform:uppercase}
.hero .btn{position:absolute;left:113px;top:403px;width:146px;height:46px;background:var(--orange);color:var(--white)}

/* section titles */
.title{position:absolute;left:0;width:1200px;text-align:center;font-family:"Roboto Condensed",sans-serif;font-weight:400;font-size:38px;color:var(--ink)}
.title b{font-weight:700}
.lead{position:absolute;left:240px;width:720px;text-align:center;font-size:12px;line-height:24px;color:var(--muted)}

/* get started */
.start{top:713px;height:516px;background:var(--white)}
.start .title{top:60px}
.start .lead{top:120px}
.plan{position:absolute;top:210px;width:394px;height:217px;background:var(--white);box-shadow:0 4px 18px rgba(0,0,0,.14)}
.plan .disc{position:absolute;left:0;top:58px;width:88px;height:100px;border-radius:0 50px 50px 0;background:#f3f3f3;display:flex;align-items:center;justify-content:center}
.plan h3{position:absolute;left:100px;top:28px;font-family:"Roboto Condensed",sans-serif;font-weight:700;font-size:24px}
.plan p{position:absolute;left:100px;top:66px;width:270px;font-size:12px;line-height:24px;color:var(--muted)}
.plan .btn{position:absolute;left:100px;top:134px;width:158px;height:42px;border:1.5px solid;font-size:11px;font-weight:500;color:var(--ink)}
.plan.business{left:188px}
.plan.business h3{color:var(--orange)}
.plan.business .btn{border-color:var(--orange)}
.plan.residential{left:655px}
.plan.residential h3{color:var(--cyan)}
.plan.residential .btn{border-color:var(--cyan)}

/* features */
.features{top:1229px;height:713px;background:var(--soft)}
.features .title{top:74px}
.features .lead{top:134px}
.feature{position:absolute;width:320px}
.feature .ico{position:absolute;left:0;top:0;width:42px;height:42px;border-radius:50%;display:flex;align-items:center;justify-content:center}
.feature h4{position:absolute;left:62px;top:2px;font-size:14px;font-weight:600;white-space:nowrap}
.feature p{position:absolute;left:62px;top:28px;width:250px;font-size:11px;line-height:24px;color:var(--muted)}
.c-cyan{background:var(--cyan)}.c-orange{background:var(--orange)}.c-magenta{background:var(--magenta)}.c-green{background:var(--green)}
.features .btn{position:absolute;left:522px;top:586px;width:155px;height:40px;border:1.5px solid var(--orange);font-size:11px;font-weight:500}

/* refer */
.refer{top:1942px;height:445px;overflow:hidden;background:var(--orange)}
.refer-photo{position:absolute;left:480px;top:0;width:720px;height:445px;background:linear-gradient(90deg,var(--orange) 0%,#d9a07a 22%,#b98a6e 50%,#8f5d4a 75%,#c44b5a 100%)}
.refer h2{position:absolute;left:113px;top:90px;font-family:"Roboto Condensed",sans-serif;font-weight:400;font-size:44px;line-height:58px;color:var(--white)}
.refer h2 strong{display:block;color:var(--magenta);font-weight:700;font-size:50px;margin-top:10px}
.refer .btn{position:absolute;left:113px;top:305px;width:150px;height:47px;border:1.5px solid var(--white);color:var(--white)}

/* reviews */
.reviews{top:2387px;height:598px;background:var(--white)}
.reviews .title{top:76px}
.reviews .lead{top:132px}
.stars{color:#f5b800;font-size:15px;letter-spacing:2px}
.reviews .score{position:absolute;left:128px;top:188px}
.review{position:absolute;background:var(--white);box-shadow:0 3px 14px rgba(0,0,0,.12);text-align:center}
.review .stars{position:absolute;left:16px;top:24px}
.review time{position:absolute;right:16px;top:26px;font-size:11px;color:var(--muted)}
.review p{position:absolute;left:20px;right:20px;top:72px;font-size:11px;line-height:23px;color:var(--muted)}
.review cite{position:absolute;left:0;right:0;top:148px;font-style:normal;font-size:12px;color:var(--orange)}
.dots{position:absolute;top:489px;left:0;width:1200px;display:flex;justify-content:center;gap:7px}
.dots span{width:8px;height:8px;border-radius:50%}

/* footer */
.footer{top:2985px;height:259px;background:var(--footer);color:#ccc}
.footer .brand{left:190px;top:40px;color:var(--orange);font-size:34px}
.footer .about{position:absolute;left:115px;top:100px;width:310px;text-align:center;font-size:11px;line-height:24px}
.footer .rule{position:absolute;top:0;width:1px;height:259px;background:#333}
.footer h5{position:absolute;top:42px;font-size:18px;font-weight:400;color:var(--white)}
.footer ul{position:absolute;left:498px;top:84px;list-style:none;font-size:11px;line-height:22.5px}
.footer .notes{position:absolute;left:678px;top:84px;width:410px;font-size:11px;line-height:24px}
.bottom{top:3244px;height:77px;background:var(--footer-dark);color:#bbb;font-size:11px}
.social{position:absolute;top:17px;width:38px;height:38px;border-radius:50%;background:var(--white);display:flex;align-items:center;justify-content:center}
.signup{position:absolute;left:491px;top:19px;width:213px;height:36px;border-radius:20px;background:var(--white);overflow:hidden}
.signup span{position:absolute;right:0;top:0;width:58px;height:36px;border-radius:20px;background:var(--magenta);color:var(--white);font-size:12px;font-weight:600;display:flex;align-items:center;justify-content:center}
.bottom .copy{position:absolute;right:113px;top:29px}
</style>
</head>
<body>

<header class="topbar">
  <div class="abs order">ORDER BY FREE PHONE : <b>0800 417 2930</b></div>
  <div class="abs account">
    <svg width="12" height="12" viewBox="0 0 12 12"><circle cx="6" cy="3.5" r="2.8" fill="#fff"/><path d="M0.5 12c0-3.3 2.4-5 5.5-5s5.5 1.7 5.5 5z" fill="#fff"/></svg>
    MY ACCOUNT
  </div>
</header>

<header class="nav">
  <div class="abs brand">quorvix</div>
  <ul class="abs menu">
    <li class="active">Home</li><li>About Us</li><li>Business</li><li>Residential</li><li>Support</li><li>Contact</li>
  </ul>
</header>

<section class="hero">
  <div class="hero-photo" role="img" aria-label="Smiling woman in glasses talking on a mobile phone in a softly lit café"></div>
  <h1>Switch To<br>Cheaper Calls Now !</h1>
  <p>Make Cheap LOCAL, NATIONAL &amp; INTERNATIONAL Unlimited Phone Calls To Your Friends, Family And More With Our Great Calling Plans.</p>
  <span class="btn">Start Here</span>
</section>

<section class="start">
  <h2 class="title">Ready to <b>Get Started</b></h2>
  <p class="lead">Lorem ipsum dolor sit amet, consectetuer adipiscing elit, sed diam nonummy nibh euismod tincidunt ut laoreet dolore magna aliquam erat volutpat. Ut wisi enim ad minim veniam, quis ullamcorper suscipit lobortis .</p>

  <article class="plan business">
    <div class="disc">
      <svg width="34" height="28" viewBox="0 0 34 28"><rect x="11" y="1" width="12" height="6" rx="2" fill="none" stroke="#f7931e" stroke-width="2.5"/><rect x="1" y="6" width="32" height="21" rx="3" fill="#f7931e"/><rect x="1" y="14" width="32" height="2" fill="#fff"/><rect x="14" y="12" width="6" height="6" fill="#fff"/></svg>
    </div>
    <h3>FOR BUSINESS</h3>
    <p>Lorem ipsum dolor sit amet, consectetuer adipiscing elit, sed dia.</p>
    <span class="btn">Get Started Now</span>
  </article>

  <article class="plan residential">
    <div class="disc">
      <svg width="32" height="30" viewBox="0 0 32 30"><path d="M16 1 2 11h28z" fill="#1ab0e6"/><rect x="5" y="11" width="22" height="18" fill="#1ab0e6"/><rect x="9" y="15" width="5" height="5" fill="#fff"/><rect x="18" y="15" width="5" height="5" fill="#fff"/><rect x="13" y="22" width="6" height="7" fill="#fff"/></svg>
    </div>
    <h3>FOR RESIDENTIAL</h3>
    <p>Lorem ipsum dolor sit amet, consectetuer adipiscing elit, sed dia.</p>
    <span class="btn">Get Started Now</span>
  </article>
</section>

<section class="features">
  <h2 class="title">Quorvix <b>Feautres &amp; Benefits</b></h2>
  <p class="lead">Lorem ipsum dolor sit amet, consectetuer adipiscing elit, sed diam nonummy nibh euismod tincidunt ut laoreet dolore magna aliquam erat volutpat. Ut wisi enim ad minim veniam, quis ullamcorper suscipit lobortis .</p>

  <div class="feature" style="left:113px;top:220px">
    <div class="ico c-cyan"><svg width="18" height="13" viewBox="0 0 18 13"><rect x="1" y="1" width="16" height="11" fill="none" stroke="#fff" stroke-width="1.6"/><path d="M1 1l8 6 8-6" fill="none" stroke="#fff" stroke-width="1.6"/></svg></div>
    <h4>FEAUTRES &amp; BENEFITS ONE</h4>
    <p>Lorem ipsum dolor sit met, consectetuer adipiscing elit, sed diam nonummy nibh euismod tincidunt aoreet dolore magna aliquam erat volutpat.</p>
  </div>
  <div class="feature" style="left:452px;top:220px">
    <div class="ico c-orange"><svg width="18" height="18" viewBox="0 0 18 18"><path d="M4 2l3 3-2 2c1 2 3 4 5 5l2-2 3 3-2 3C7 16 2 11 1 5z" fill="#fff"/></svg></div>
    <h4>FEAUTRES &amp; BENEFITS ONE</h4>
    <p>Lorem ipsum dolor sit met, consectetuer adipiscing elit, sed diam nonummy nibh euismod tincidunt aoreet dolore magna aliquam erat volutpat.</p>
  </div>
  <div class="feature" style="left:788px;top:220px">
    <div class="ico c-magenta"><svg width="18" height="18" viewBox="0 0 18 18"><circle cx="9" cy="7" r="2" fill="#fff"/><path d="M9 9v8M4 3a7 7 0 0 0 0 8M14 3a7 7 0 0 1 0 8" fill="none" stroke="#fff" stroke-width="1.6"/></svg></div>
    <h4>FEAUTRES &amp; BENEFITS ONE</h4>
    <p>Lorem ipsum dolor sit met, consectetuer adipiscing elit, sed diam nonummy nibh euismod tincidunt aoreet dolore magna aliquam erat volutpat.</p>
  </div>
  <div class="feature" style="left:113px;top:384px">
    <div class="ico c-magenta"><svg width="18" height="16" viewBox="0 0 18 16"><path d="M2 1h14v10H7l-4 4v-4H2z" fill="none" stroke="#fff" stroke-width="1.6"/></svg></div>
    <h4>FEAUTRES &amp; BENEFITS ONE</h4>
    <p>Lorem ipsum dolor sit met, consectetuer adipiscing elit, sed diam nonummy nibh euismod tincidunt aoreet dolore magna aliquam erat volutpat.</p>
  </div>
  <div class="feature" style="left:452px;top:384px">
    <div class="ico c-green"><svg width="18" height="18" viewBox="0 0 18 18"><path d="M4 2l3 3-2 2c1 2 3 4 5 5l2-2 3 3-2 3C7 16 2 11 1 5z" fill="#fff"/></svg></div>
    <h4>FEAUTRES &amp; BENEFITS ONE</h4>
    <p>Lorem ipsum dolor sit met, consectetuer adipiscing elit, sed diam nonummy nibh euismod tincidunt aoreet dolore magna aliquam erat volutpat.</p>
  </div>
  <div class="feature" style="left:788px;top:384px">
    <div class="ico c-orange"><svg width="18" height="18" viewBox="0 0 18 18"><circle cx="9" cy="7" r="2" fill="#fff"/><path d="M9 9v8M4 3a7 7 0 0 0 0 8M14 3a7 7 0 0 1 0 8" fill="none" stroke="#fff" stroke-width="1.6"/></svg></div>
    <h4>FEAUTRES &amp; BENEFITS ONE</h4>
    <p>Lorem ipsum dolor sit met, consectetuer adipiscing elit, sed diam nonummy nibh euismod tincidunt aoreet dolore magna aliquam erat volutpat.</p>
  </div>

  <span class="btn">View All Feautres</span>
</section>

<section class="refer">
  <div class="refer-photo" role="img" aria-label="Two smiling young women looking at a smartphone together"></div>
  <h2>REFER A FRIEND AND<br>GET 2 MONTHS<strong>FREE CALL PACKAGE</strong></h2>
  <span class="btn">Start Here</span>
</section>

<section class="reviews">
  <h2 class="title">Customer <b>Review</b></h2>
  <p class="lead">Lorem ipsum dolor sit amet, consectetuer adipiscing elit, sed diam nonummy nibh euismod tincidunt ut laoreet dolore magna aliquam erat volutpat. Ut wisi enim ad minim veniam, quis nostrud exerci tation ullamcorper suscipit lobortis .</p>
  <div class="stars score">★★★★★</div>

  <article class="review" style="left:113px;top:228px;width:305px;height:192px">
    <time>26.03.2018</time>
    <p>I'm more likely to just pick up the phone... Instead of using email, I now speak to people. just pick up the phone...</p>
    <cite>Harriet K. Ellis</cite>
  </article>
  <article class="review" style="left:447px;top:219px;width:304px;height:216px">
    <div class="stars">★★★★★</div>
    <time>26.03.2018</time>
    <p>I'm more likely to just pick up the phone... Instead of using emails I now speak to people. just pick up the phone...</p>
    <cite>Harriet K. Ellis</cite>
  </article>
  <article class="review" style="left:779px;top:219px;width:306px;height:216px">
    <div class="stars">★★★★★</div>
    <time>26.03.2018</time>
    <p>I'm more likely to just pick up the phone... Instead of using email I now speak to people. just pick up the phone...</p>
    <cite>Harriet K. Ellis</cite>
  </article>

  <div class="dots"><span style="background:var(--magenta)"></span><span style="background:var(--cyan)"></span><span style="background:var(--orange)"></span><span style="background:#555"></span></div>
</section>

<footer class="footer">
  <div class="abs brand">quorvix</div>
  <p class="about">Lorem ipsum dolor sit amet, consectetuer adipiscing elit, sed diam nonummy nibh euismod tincidunt ut laoreet dolore magna aliquam erat volutpat. nibh euismod tincidunt</p>
  <div class="rule" style="left:456px"></div>
  <div class="rule" style="left:642px"></div>
  <h5 style="left:498px">Company</h5>
  <ul><li>Home</li><li>About Us</li><li>Business</li><li>Residential</li><li>Support</li><li>Contact</li></ul>
  <h5 style="left:678px">Notes For You</h5>
  <p class="notes">‡Applies to UK landline numbers starting with 01, 02 and 03. International landlines calls to countries in our call plans are unlimited and do not include calls to mobiles unless specified.<br>Calls are billed on a per second increment. Fair usage policy applies.</p>
</footer>

<footer class="bottom">
  <span class="social" style="left:109px" aria-label="Social link">
    <svg width="18" height="16" viewBox="0 0 18 16"><path d="M2 1h14v10H7l-4 4v-4H2z" fill="#1a1a1a"/></svg>
  </span>
  <span class="social" style="left:160px" aria-label="Social link">
    <svg width="18" height="18" viewBox="0 0 18 18"><circle cx="4" cy="9" r="2.6" fill="#1a1a1a"/><circle cx="14" cy="4" r="2.6" fill="#1a1a1a"/><circle cx="14" cy="14" r="2.6" fill="#1a1a1a"/><path d="M4 9l10-5M4 9l10 5" stroke="#1a1a1a" stroke-width="1.6"/></svg>
  </span>
  <div class="signup"><span>GO</span></div>
  <div class="copy">© All Rights Reserved 2018.</div>
</footer>

</body>
</html>
```